Homepage Banner- Fashion Jewelry Wholesale Company

Homepage Banner

Company Background: Velma Trinkets is a leading provider of high fashion costume (NOT fine) jewelry. Serving the junior mall and specialty chain stores, we constantly have the pulse on trends. We serve the teenage to young adults market through our retail channels, such as; Ninety Pine, Dapper Delphine, Marisol grove & many more. Some of our latest trends include Boho, metallic tattoos, body jewelry, layered necklaces and much more.

Examples of high fashion costume jewelry:
• http://www.openwillow.example/necklines/
• https://www.quillbayoutlet.example/shop/Women/Jewelry/Fashion%20Jewelry
• http://www.marisolgrove.example/thumbnail/Accessories/Jewelry-Watches/pc/2116/2598.uts
• http://www.ninetypine.example/Product/Category.aspx?br=np9&category=acc_jewelry&pagesize=60&page=1

Direction:
• Photo size: 930 X 624 pixels
• JPEG
• Sourcing and/ or creating key elements (prints, typography, photos)
• Establish a graphic theme, colors, background image, patterns, fonts, etc. that represents the business and the products we sell
• Sleek design with high fashion in mind
• White/ light color background
• Display Velma Trinkets with cool, high fashion font
• Underneath Velma Trinkets write “a division of Banyard Gem Corp”

Target Market(s)

Female: young adults

Industry/Entity Type

Fashion

Number of Pages Required

1 page

Font styles to use
Decorative
Script

Requirements
Must have
• Incorporate some fashion jewelry pieces
Nice to have
• Model wearing fashion jelwery
Should not have
• No fine jewelry

```html
<!DOCTYPE html>
<html lang="en">
<head>
<meta charset="utf-8">
<title>Velma Trinkets – Dream Jewellery</title>
<link rel="stylesheet" href="https://fonts.googleapis.com/css2?family=Raleway:wght@300;400&family=Lora:ital,wght@0,500;1,400&display=swap">
<style>
  :root {
    --paper: #ffffff;
    --ink: #2b2b2b;
    --ink-soft: #3a3a3a;
    --magenta: #b0307a;
    --rule: #9a9a9a;
    --button: #262626;
    --button-text: #ffffff;
    --photo-navy: #1d2a55;
    --photo-teal: #3fa6c4;
    --photo-pink: #d0507e;
  }
  * { margin: 0; padding: 0; box-sizing: border-box; }
  html, body {
    width: 1200px;
    height: 805px;
    overflow: hidden;
    background: var(--paper);
  }
  .banner {
    position: relative;
    width: 1200px;
    height: 805px;
    background: var(--paper);
    overflow: hidden;
  }
  .brand {
    position: absolute;
    left: 129px;
    top: 68px;
  }
  .brand-name {
    display: block;
    font-family: "Raleway", sans-serif;
    font-weight: 300;
    font-size: 44px;
    line-height: 1;
    color: var(--ink);
    padding-bottom: 22px;
    border-bottom: 1px solid var(--rule);
  }
  .brand-parent {
    display: block;
    margin-top: 14px;
    font-family: "Raleway", sans-serif;
    font-weight: 400;
    font-size: 17px;
    color: var(--magenta);
  }
  .headline {
    position: absolute;
    left: 100px;
    top: 292px;
    font-family: "Raleway", sans-serif;
    font-weight: 300;
    font-size: 60px;
    line-height: 66px;
    text-transform: uppercase;
  }
  .headline-accent { display: block; color: var(--magenta); letter-spacing: 13px; }
  .headline-main { display: block; color: var(--ink); letter-spacing: 0.5px; }
  .tagline {
    position: absolute;
    left: 101px;
    top: 434px;
    width: 305px;
    font-family: "Lora", serif;
    font-style: italic;
    font-size: 22px;
    line-height: 32px;
    color: var(--ink-soft);
  }
  .shop-button {
    position: absolute;
    left: 101px;
    top: 552px;
    width: 200px;
    height: 59px;
    background: var(--button);
    color: var(--button-text);
    font-family: "Lora", serif;
    font-weight: 500;
    font-size: 22px;
    letter-spacing: 1.5px;
    text-transform: uppercase;
    text-decoration: none;
    display: flex;
    align-items: center;
    justify-content: center;
  }
  .model-photo {
    position: absolute;
    left: 471px;
    top: 0;
    width: 729px;
    height: 805px;
    background:
      radial-gradient(ellipse at 35% 45%, var(--photo-teal) 0%, transparent 45%),
      radial-gradient(ellipse at 70% 60%, var(--photo-pink) 0%, transparent 40%),
      linear-gradient(160deg, #2a3670 0%, var(--photo-navy) 60%, #141c3d 100%);
  }
</style>
</head>
<body>
  <main class="banner">
    <div class="brand">
      <span class="brand-name">Velma Trinkets</span>
      <span class="brand-parent">a division of Banyard Gem Corp</span>
    </div>

    <h1 class="headline">
      <span class="headline-accent">Dream</span>
      <span class="headline-main">Jewellery</span>
    </h1>

    <p class="tagline">Class aptent taciti sociosqu ad litora torquent per conu bia nostra per ince</p>

    <a class="shop-button" href="#">Shop Now</a>

    <div class="model-photo" role="img" aria-label="Two models in bold tropical-print navy outfits wearing chunky statement necklaces and floral headpieces"></div>
  </main>
</body>
</html>
```